Clean Modern Skin Product branding/ label.

I need a label for a skincare line. The company is Velmora but product names will vary. A couple products to list are:
Sensitive Cleanser, Tevola, Ostiva, Malo ve, Quintel, Quintel Plus, Quintel Intense, Dovira, Ambrel and Fenwyn.

I would like the color scheme to be muted greens, grays, tourquise. The bottles are white, boston shaped with pumps, and ounces are 2, 4, 8, 16 ounces. When I choose the design, I can give you exact label sizes. Along with the ingredience already on the product label.

The look I desire is clean, minimal. A modern, organic look. Ideas that come to mind are a Ostrelle,https://www.ostrelle-beauty.example/product/1573/15501/3-step/step-2-exfoliate/clarifying-lotion-1 and the simplicity of Vo Tenn.

Both styles high light the name, in this case Velmora, and then the specific product.

My product is clean utilizing pure ingredients rather that a bunch fillers and binders. When I work with my clients I normally will say we need to "restore the balance" from over use of harsh products. That is why this lines works. It restores the skin to it's natural state. The process is simple, so I would like the label to reflect that simplicity.

Target Market(s)

Anyone with sensitive skin. So gender neutral

Industry/Entity Type

Skin Care Product

Font styles to use
Serif
Sans Serif
Decorative

Colors
acd037
33b8a4
fcfefd
85cae6
d3d3d3

Requirements
Must have
• Logo, name of product and color identity for cleanser, Active products, moisturizers
• I am thinking we could have one color for a cleanser and a space where I can put a sticker on which cleanser it is. Acne Cleasner, Sensitive Cleanser, and Cleanser.
Nice to have
• Not sure....suprise me. I would like the font to stay the same on the VELMORA, but you can change color, or color of leaf.
Should not have
• Too busy, too crowded or look like every other skincare line

```html
<!DOCTYPE html>
<html lang="en">
<head>
<meta charset="utf-8">
<title>Velmora – Sensitive Cleanser Label</title>
<link rel="stylesheet" href="https://fonts.googleapis.com/css2?family=Roboto:wght@100;300;500;700&display=swap">
<style>
  :root {
    --backdrop: #e9eeee;
    --label-white: #ffffff;
    --leaf-green: #7cd321;
    --tagline-mint: #6fe3bf;
    --name-grey: #5a5d60;
    --product-grey: #4a4a4a;
    --rule-mint: #9fe6cf;
    --size-ink: #1d1d1d;
  }
  * { box-sizing: border-box; margin: 0; padding: 0; }
  html, body {
    width: 1200px;
    height: 1200px;
    overflow: hidden;
    background: var(--backdrop);
  }
  .canvas {
    position: relative;
    width: 1200px;
    height: 1200px;
  }
  .label {
    position: absolute;
    left: 118px;
    top: 50px;
    width: 964px;
    height: 1100px;
    background: var(--label-white);
    box-shadow: 0 8px 24px rgba(0, 0, 0, 0.12);
    font-family: "Roboto", Arial, sans-serif;
  }
  .brand-dot {
    position: absolute;
    left: 432px;
    top: 108px;
    width: 100px;
    height: 100px;
    border-radius: 50%;
    background: var(--leaf-green);
  }
  .tagline {
    position: absolute;
    left: 0;
    right: 0;
    top: 268px;
    text-align: center;
    font-weight: 700;
    font-size: 35px;
    color: var(--tagline-mint);
    letter-spacing: 0.2px;
  }
  .brand-name {
    position: absolute;
    left: 0;
    right: 0;
    top: 320px;
    text-align: center;
    font-weight: 500;
    font-size: 150px;
    line-height: 1.1;
    color: var(--name-grey);
    letter-spacing: -2px;
  }
  .product-name {
    position: absolute;
    left: 182px;
    width: 600px;
    top: 592px;
    padding: 6px 0 4px;
    border-top: 2px solid var(--rule-mint);
    border-bottom: 2px solid var(--rule-mint);
    text-align: center;
    font-weight: 100;
    font-size: 70px;
    line-height: 1;
    color: var(--product-grey);
  }
  .net-volume {
    position: absolute;
    right: 207px;
    top: 990px;
    font-weight: 700;
    font-size: 38px;
    color: var(--size-ink);
  }
</style>
</head>
<body>
  <main class="canvas">
    <section class="label">
      <div class="brand-dot"></div>
      <p class="tagline">restore the balance</p>
      <h1 class="brand-name">Velmora</h1>
      <h2 class="product-name">Sensitive Cleanser</h2>
      <p class="net-volume">16 oz.</p>
    </section>
  </main>
</body>
</html>
```